WordPress Template
Ravenfield Staffing, Inc.
Thank you all for you designs! A lot of great ideas, and I appreciate your effort.
Re: 94, thank you, but the image doesn't really work for me.
Re: 71 and similar -- very nice! I'm going to get feedback from others on my team about those and the others I haven't eliminated. Thank you!
Re: 61 and similar, thank you, but that image doesn't work for me.
Re: 57, can I see that with the oval steps you did in 44? Thanks!
Re: 75-78, thank you, but I don't like the image with the people.
thanks,
BrightquillStudio
On 55 and 56, I think I prefer the image to be next to the words, as in 44. Making the star red is nice little touch, and I do like the smaller stars rather than the larger as in 44. Thanks!
On 46, thank you. Overall, I like the look and feel of it. I'm thinking about the upper right corner image...maybe a slightly smaller star? I"m not sure if I'm going to be on all the social media or not, so the bottom left will need something there if not.
On 51, I like the ladder since it plays off the idea of climbing the ladder of success, but would it be possible to do a ladder that's a bit less real looking? Thanks!
Re: 47-54, thank you! I've eliminated the ones where the images don't work for me for whatever reason. I like the overall layout and design, but would like to see a bit more red and/or other contrast to punch it up a bit. Thanks so much!
***The font in the logo is Geosans Light, and I'd like no more than 2 fonts total in the design (so Geosans Light plus one other).*** Thank you!
On 25, can you play with the colors a bit and get rid of the Shape Your Morning on the far right top? Also I'm not keen on the look of that menu bar. Thanks!
On 40, can you add in a figure on the stairs or maybe just the figure using the star/endless possibilities concept on the bottom right or in the middle right someplace? And omit the second logo on the far left in the middle. And instead of the Shape Your Morning restated in the middle next to the second logo image, let's use The Possibilities are Endless, You Just Have to Know Where to Look. Thank you!
Re: 38, thank you, the figure on the stairs is moving in the right direction, I think. What about eliminating the building part? And/or maybe moving the figure/stairs to the bottom by the text? Thanks!
Thank you for 33-37. Please note my prior comments on not wanting to include the Shape Your Morning on the top right from the old design. Overall, I'm not sure any of these really grab me...although I do want simple, these are all very plain looking. Thank you for submitting, though.
Hi PH,
please feel free to let me know the required changes so that your expectations are met.
Awaiting for your kind feedback
Polaris
Thank you for 26-31. None of those are really working....I think having the image on both top and bottom looks too busy, and please omit the old "shape your morning" on the top right. I think using some version of the figure in the D is probably the way to go, but the overall look of 25 doesn't really work. Thank you!
What about something that uses the little figure from the D on the logo, combined with some sort of concept of limitlessness? This instead of the figure from the old site....
Hi,
I think the old graphic shouldn't be a prob as that seems very abstract that depict growth and success.
Thank you for 22 - 24. Please, no actual images of people for reasons stated previously. Also not very keen on random clip-art looking images as used on the bottom. I really like a clean style. I see what you were doing with the stairs to the right, but with the guy climbing up them, it just looks like hard work again. The image in the old site looks whimsical and "reach for the stars" instead of the hard work of climbing stairs.
On 21, I think we also need to get rid of the Shape Your Morning on the far right (the one that's left over from the old site). Also, it does look odd without another graphic to the right of the text, but I just don't really think the old graphic works with the new logo.
Hi, No graphics means. Did you mean about the footer, the background I used?
Maybe something that has just the logo and the text without any other graphics?
Thank you for #20. I think I may have to let go of using that old figure....it just doesn't seem to work with the new vibe of the new logo, yet I'm not sure what to replace it with. But thank you for listening to my comments; this is a very good version based on what I was asking for, but I just don't know if it works.

```html
<!DOCTYPE html>
<html lang="en">
<head>
<meta charset="utf-8">
<title>Ravenfield Staffing, Inc.</title>
<link rel="stylesheet" href="https://fonts.googleapis.com/css2?family=Didact+Gothic&family=Open+Sans:wght@400;600&display=swap">
<style>
  :root {
    --brand-red: #8e1b1f;
    --accent-red: #c3262b;
    --nav-dark: #7a1418;
    --ink: #55585c;
    --ink-soft: #6d7074;
    --rule-grey: #c9c9c9;
    --paper: #ffffff;
    --paper-shade: #e4e4e4;
  }
  * { margin: 0; padding: 0; box-sizing: border-box; }
  html, body { width: 1200px; height: 818px; overflow: hidden; background: var(--paper); }
  body { position: relative; font-family: "Open Sans", sans-serif; color: var(--ink); }

  .site-header {
    position: absolute; left: 0; top: 0; width: 1200px; height: 300px;
    background:
      linear-gradient(90deg, var(--paper-shade) 0%, #f6f6f6 8%, #ffffff 30%, #ffffff 70%, #f4f4f4 92%, var(--paper-shade) 100%);
  }
  .brand { position: absolute; left: 108px; top: 118px; }
  .brand-name {
    display: flex; align-items: center; gap: 16px;
    font-family: "Didact Gothic", sans-serif; font-size: 42px; color: var(--brand-red);
    letter-spacing: 0.5px;
  }
  .brand-dot { width: 38px; height: 38px; border-radius: 50%; background: var(--brand-red); }
  .brand-tagline {
    margin: 14px 0 0 56px;
    font-family: "Didact Gothic", sans-serif; font-size: 22px; letter-spacing: 9px;
    color: var(--ink); text-transform: uppercase;
  }

  .main-nav {
    position: absolute; left: 36px; top: 300px; width: 1128px; height: 48px;
    background: radial-gradient(ellipse 40% 120% at 50% 50%, var(--accent-red) 0%, var(--brand-red) 55%, var(--nav-dark) 100%);
    display: flex; align-items: center;
  }
  .main-nav a {
    position: absolute; color: #fff; text-decoration: none; font-size: 17px;
  }

  .intro { position: absolute; left: 89px; top: 400px; width: 660px; }
  .intro-headline {
    font-family: "Didact Gothic", sans-serif; font-weight: 400;
    font-size: 46px; line-height: 46px; color: var(--ink); letter-spacing: -0.5px;
  }
  .intro-headline em { font-style: normal; color: var(--accent-red); }
  .intro-copy { margin-top: 26px; font-size: 12.5px; line-height: 18px; color: var(--ink-soft); }
  .intro-copy + .intro-copy { margin-top: 14px; }

  .hero-art {
    position: absolute; left: 852px; top: 444px; width: 252px; height: 204px; border-radius: 12px;
    background: radial-gradient(ellipse at 70% 40%, #e9e9e9 0%, #f6f6f6 60%, #ffffff 100%);
  }

  .footer-rule { position: absolute; left: 36px; top: 712px; width: 1128px; height: 1px; background: var(--rule-grey); }
  .footer-rule-accent { position: absolute; left: 636px; top: 710px; width: 528px; height: 4px; background: var(--accent-red); }
  .footer-nav { position: absolute; left: 41px; top: 744px; display: flex; gap: 22px; }
  .footer-nav a { color: var(--ink-soft); text-decoration: none; font-size: 12px; }
  .footer-mark {
    position: absolute; left: 690px; top: 738px; font-family: "Didact Gothic", sans-serif;
    font-size: 13px; color: var(--brand-red); width: 66px; line-height: 15px;
  }
  .footer-credit { position: absolute; left: 770px; top: 738px; font-size: 11px; line-height: 16px; color: var(--ink-soft); }
</style>
</head>
<body>
  <header class="site-header">
    <div class="brand">
      <div class="brand-name"><span class="brand-dot"></span>Ravenfield Staffing, Inc.</div>
      <div class="brand-tagline">Shape Your Morning</div>
    </div>
  </header>

  <nav class="main-nav">
    <a href="#" style="left:312px">Home</a>
    <a href="#" style="left:396px">Your Team</a>
    <a href="#" style="left:511px">Our Mission</a>
    <a href="#" style="left:636px">Attorneys</a>
    <a href="#" style="left:744px">Law Firms</a>
    <a href="#" style="left:852px">Contact</a>
  </nav>

  <section class="intro">
    <h1 class="intro-headline">The possibilities are endless:<br>You <em>JUST</em> need to know<br>where to <em>LOOK</em></h1>
    <p class="intro-copy">And that's what we're here for. We can help you find a new position within your current profession, or we can provide advice to help to discover your true path to happiness.</p>
    <p class="intro-copy">We're here for you. We want a good match for both our candidates and our clients: It's YOUR career. . . and YOUR law firm.</p>
  </section>

  <div class="hero-art" role="img" aria-label="Illustration of a small figure stepping up floating oval steps toward a red star"></div>

  <div class="footer-rule"></div>
  <div class="footer-rule-accent"></div>
  <nav class="footer-nav">
    <a href="#">Home</a><a href="#">Your Team</a><a href="#">Our Mission</a><a href="#">Attorneys</a><a href="#">Law Firms</a><a href="#">Contact</a>
  </nav>
  <div class="footer-mark">Ravenfield</div>
  <p class="footer-credit">Copyright © 2015 Ravenfield Recruiting | Visit Halloway Publishing<br>Brand Strategy by Marlow Finch Communications, Inc.</p>
</body>
</html>
```